Etiketten für Rotwein
Zielgruppe
Wir starten dieses Jahr mit unserem ersten Rotwein unserer neuen Marke CAL VEDRINAS aus unserem neuen Weingut auf Mallorca.
Es folgen in den kommenden Jahren ein Rosé und weitere Weißweine.
Aufgabenstellung
Wir suchen ein Design für unser erstes Flaschenetikett der Rotweinflaschen.
Die Höhe soll maximal 130 mm sein.
Der Name soll 'Fermino' sein.
Die Rebsorte 'Cabernet Sauvignon' und der Jahrgang '2025' sollen mit erscheinen.
Unser Logo sollte mit integriert werden.
Das Erscheinungsbild soll edel, elegant, markant, präsent, wieder erkennbar und einzigartig sein.
Es gibt ein paar Ideen, diese sind aber nur als Hinweise zu verstehen, die verwendet werden könnten.
Dies sind 2 Teddybären im Weinfeld, Teddybären auf einem Traktor im Weinfeld/ Weinberg, Landschaft oder eben komplett etwas anderes Kreatives.
Die Anlagen sind unser Logo in 3 Varianten und einige Beispiele von eigenen unprofessionellen Versuchen, sowie tolle Etikettendesigns die uns gefallen.
We are looking for a design for our first red wine bottle label.
The maximum height should be 130mm.
The name should be 'Fermino'.
The grape variety 'Cabernet Sauvignon' and the vintage 2025 should also be included.
Our logo should be integrated.
The overall look should be sophisticated, elegant, striking, memorable, recognizable, and unique.
We have a few ideas, but these are just suggestions that could be used.
These include two teddy bears in a vineyard, teddy bears on a tractor in a vineyard, a landscape, or something completely different and creative.
Attached are our logo in three variations, some examples of our own unprofessional attempts, and some great label designs that we like.
Jens & Uwe
Cal Vedrinas

```html
<!DOCTYPE html>
<html lang="de">
<head>
<meta charset="utf-8">
<title>Fermino – Cabernet Sauvignon 2025 – Cal Vedrinas</title>
<link rel="stylesheet" href="https://fonts.googleapis.com/css2?family=Pinyon+Script&family=Playfair+Display:wght@400;700&display=swap">
<style>
  :root {
    --bg: #1b1720;
    --label-line: #b9b5bf;
    --gold: #e2b24c;
    --cream: #f1e2c6;
    --white: #f4f1ec;
    --orange-deep: #e2400c;
    --orange: #ff7a00;
    --amber: #ffb300;
  }
  html, body {
    margin: 0;
    padding: 0;
    width: 1200px;
    height: 1200px;
    overflow: hidden;
    background: var(--bg);
  }
  .canvas {
    position: relative;
    width: 1200px;
    height: 1200px;
    background: var(--bg);
  }
  .wine-label {
    position: absolute;
    left: 398px;
    top: 309px;
    width: 404px;
    height: 583px;
    box-sizing: border-box;
    border: 1px solid var(--label-line);
    background: var(--bg);
  }
  .sunburst {
    position: absolute;
    left: 66px;
    top: 67px;
    width: 270px;
    height: 270px;
    border-radius: 50%;
    background: radial-gradient(circle,
      rgba(27,23,32,1) 0%,
      rgba(27,23,32,1) 30%,
      rgba(255,179,0,0.22) 42%,
      rgba(255,122,0,0.28) 70%,
      rgba(226,64,12,0.12) 90%,
      rgba(27,23,32,0) 100%);
  }
  .brand-ring {
    position: absolute;
    left: 127px;
    top: 128px;
    width: 148px;
    height: 148px;
    box-sizing: border-box;
    border: 2px solid var(--gold);
    border-radius: 50%;
  }
  .brand-name {
    position: absolute;
    left: 0;
    width: 100%;
    text-align: center;
    font-family: "Playfair Display", serif;
    font-weight: 700;
    color: var(--gold);
    margin: 0;
  }
  .brand-name--main {
    top: 188px;
    font-size: 11.5px;
    letter-spacing: 0.6px;
  }
  .brand-name--place {
    top: 206px;
    font-size: 7px;
    letter-spacing: 0.8px;
  }
  .wine-name {
    position: absolute;
    left: 0;
    width: 384px;
    top: 360px;
    margin: 0;
    text-align: center;
    font-family: "Pinyon Script", cursive;
    font-weight: 400;
    font-size: 74px;
    line-height: 1;
    background: linear-gradient(180deg, var(--orange-deep) 0%, var(--orange) 60%, var(--amber) 100%);
    -webkit-background-clip: text;
    background-clip: text;
    color: transparent;
  }
  .grape {
    position: absolute;
    left: 0;
    width: 100%;
    top: 455px;
    margin: 0;
    text-align: center;
    font-family: "Playfair Display", serif;
    font-weight: 400;
    font-size: 18px;
    color: var(--cream);
    letter-spacing: 0.2px;
  }
  .vintage {
    position: absolute;
    left: 0;
    width: 100%;
    top: 485px;
    margin: 0;
    text-align: center;
    font-family: "Playfair Display", serif;
    font-weight: 400;
    font-size: 12px;
    color: var(--white);
  }
</style>
</head>
<body>
  <div class="canvas">
    <section class="wine-label">
      <div class="sunburst" role="img" aria-label="Sonnenkranz aus gepunkteten Strahlen in Orange und Gold"></div>
      <div class="brand-ring"></div>
      <p class="brand-name brand-name--main">CAL VEDRINAS</p>
      <p class="brand-name brand-name--place">MALLORCA</p>
      <h1 class="wine-name">Fermino</h1>
      <p class="grape">Cabernet Sauvignon</p>
      <p class="vintage">2025</p>
    </section>
  </div>
</body>
</html>
```